2-sided DL financial services marketing brochure

We need a 2-sided DL sized brochure which will be used by partner businesses to offer our services to their clients.

Design files must be delivered in Adobe Indesign CS5 compatible format

We would like brochure to look/feel similar to our new website, a sample of which can be seen here:

http://kobera.taldrix.cc/

Current company website is here

www.kobera.com.au

Brochure content, company logo and brand guidelines attached. Happy to consider changes to content if it will aid in design without compromising clarity of message.

We have a large selection of stock photography available for used in chosen design. For purposes of bidding, please just use sample photography or send through requests for specific style of image(s)

Target Market(s)

Families with debt. Pre-retirees. Retirees

Industry/Entity Type

Financial

Other font styles liked:
• See website links and design guidelines doc

Requirements
Must have
• Company logo. Content supplied

```html
<!DOCTYPE html>
<html lang="en">
<head>
<meta charset="utf-8">
<title>Kobera – Financial Health Brochure</title>
<link href="https://fonts.googleapis.com/css2?family=Source+Sans+3:wght@400;600;700;800&display=swap" rel="stylesheet">
<style>
  :root {
    --plum: #6e2a6c;
    --berry: #8e1f52;
    --berry-deep: #7a1845;
    --ink: #3b3b3b;
    --panel: rgba(255, 255, 255, 0.82);
    --white: #ffffff;
  }
  * { margin: 0; padding: 0; box-sizing: border-box; }
  html, body { width: 1200px; height: 2544px; overflow: hidden; background: var(--white); }
  body { font-family: "Source Sans 3", Arial, sans-serif; color: var(--ink); }

  .brochure { position: relative; width: 1200px; height: 2544px; }

  .feature { position: absolute; left: 0; width: 1200px; height: 716px; overflow: hidden; }
  .feature--ready { top: 0; }
  .feature--know { top: 730px; }
  .feature--report { top: 1460px; }

  .photo { position: absolute; inset: 0; }
  .photo--family { background: linear-gradient(100deg, #c9a58d 0%, #e8d6c6 40%, #f4efe9 70%, #f7f4f1 100%); }
  .photo--woman { background: linear-gradient(100deg, #5a3a2c 0%, #b08a74 30%, #e7ddd4 60%, #f5f1ed 100%); }
  .photo--couple { background: linear-gradient(100deg, #d8c3a6 0%, #c79d80 35%, #eadfd3 65%, #f6f2ee 100%); }

  .panel {
    position: absolute; right: 40px; width: 540px;
    background: var(--panel); padding: 40px 36px;
    text-align: center;
  }
  .feature--ready .panel { top: 90px; }
  .feature--know .panel { top: 80px; }
  .feature--report .panel { top: 70px; }

  .panel__title {
    font-weight: 800; font-size: 46px; line-height: 1.05;
    color: var(--berry); letter-spacing: 0.5px; margin-bottom: 18px;
  }
  .panel__rule { height: 2px; background: rgba(142, 31, 82, 0.25); margin: 0 0 18px; }
  .panel__text { font-size: 28px; line-height: 1.32; }
  .panel__text + .panel__text { margin-top: 20px; }

  .bullets { list-style: none; margin-top: 12px; font-size: 28px; line-height: 1.4; }
  .bullets li::before { content: "• "; }

  .steps { list-style: none; font-size: 28px; line-height: 1.3; }
  .steps li { margin-bottom: 12px; }

  .divider { position: absolute; left: 0; width: 1200px; height: 44px; z-index: 2; }
  .divider--one { top: 708px; }
  .divider--two { top: 1438px; }

  .footer {
    position: absolute; left: 0; top: 2176px; width: 1200px; height: 368px;
    background: linear-gradient(180deg, var(--berry) 0%, var(--berry-deep) 100%);
    color: var(--white); text-align: center; padding-top: 70px;
  }
  .footer__lead { font-size: 32px; }
  .footer__link { font-size: 34px; font-weight: 700; margin-top: 4px; }
  .brand { margin-top: 56px; display: flex; justify-content: center; align-items: center; gap: 18px; }
  .brand__name { font-size: 92px; font-weight: 700; line-height: 1; color: var(--white); }
  .brand__mark { width: 34px; height: 34px; background: var(--white); }
</style>
</head>
<body>
<main class="brochure">

  <section class="feature feature--ready">
    <div class="photo photo--family" role="img" aria-label="Smiling mother hugging her young daughter"></div>
    <div class="panel">
      <h2 class="panel__title">ARE YOU READY?</h2>
      <p class="panel__text">Life’s journey is full of change, both planned and unplanned:</p>
      <ul class="bullets">
        <li>Purchasing a home</li>
        <li>Raising a family</li>
        <li>Career changes</li>
        <li>Retirement</li>
        <li>Unexpected injury (or illness)</li>
      </ul>
    </div>
  </section>

  <svg class="divider divider--one" viewBox="0 0 1200 44" aria-hidden="true">
    <rect x="0" y="0" width="1200" height="22" fill="#6e2a6c"/>
    <polygon points="565,22 635,22 600,44" fill="#6e2a6c"/>
  </svg>

  <section class="feature feature--know">
    <div class="photo photo--woman" role="img" aria-label="Thoughtful woman wearing glasses"></div>
    <div class="panel">
      <h2 class="panel__title">DO YOU KNOW?</h2>
      <ol class="steps">
        <li>1. Your current and future<br>net wealth</li>
        <li>2. Your cash flow and how<br>much tax you pay</li>
        <li>3. When your mortgage<br>will be paid off</li>
        <li>4. Your likely retirement income</li>
        <li>5. Whether you have adequate<br>personal protection</li>
      </ol>
    </div>
  </section>

  <svg class="divider divider--two" viewBox="0 0 1200 44" aria-hidden="true">
    <rect x="0" y="0" width="1200" height="22" fill="#6e2a6c"/>
    <polygon points="565,22 635,22 600,44" fill="#6e2a6c"/>
  </svg>

  <section class="feature feature--report">
    <div class="photo photo--couple" role="img" aria-label="Laughing young couple embracing"></div>
    <div class="panel">
      <h2 class="panel__title">COMPLIMENTARY<br>FINANCIAL HEALTH<br>REPORT</h2>
      <div class="panel__rule"></div>
      <p class="panel__text">Kobera’s Financial Health report shows you where you are today and where you’re heading.</p>
      <p class="panel__text">If there’s a gap between your expectations and reality, it’s better to know sooner rather than later!</p>
    </div>
  </section>

  <footer class="footer">
    <p class="footer__lead">Check out a sample report at</p>
    <p class="footer__link">www.kobera.com.au/my-financial-health</p>
    <div class="brand">
      <span class="brand__name">kobera</span>
      <span class="brand__mark" aria-hidden="true"></span>
    </div>
  </footer>

</main>
</body>
</html>
```